looking for sleek business card to standout from the crowd!

We are a young biotechnology company looking to help you personalize your health through understanding your genetic make up. We need you help in making a clean but sleek business card design using our new logo. The goal? Any time we give our cards out, people say "nice card!" The feel we are going for is "modern-techy". We don't want to come across as an old, giant pharma company, but not trying to be a hipster either.

Target Market(s)

healthcare and biotechnology industry.

Industry/Entity Type

Biotechnology

Contact Information for Business Card

Info to include on the card will be NAME, TITLE, EMAIL, PHONE. The companies website (www.corvalinbio.com) should also be on the card some where. Would like the logo, when printed, to be raised.

Requirements
Must have
• The logo we have attached in the color it is in. Fonts for text should lean toward more professional/tech.
Nice to have
• Prefer white/light color background
Should not have
• cartoons, landscape backgrounds images.

```html
<!DOCTYPE html>
<html lang="en">
<head>
<meta charset="utf-8">
<title>Corvalin Business Card</title>
<link href="https://fonts.googleapis.com/css2?family=Exo+2:wght@600;700&display=swap" rel="stylesheet">
<style>
  :root {
    --brand-blue: #0a7bd0;
    --brand-green: #8fd04a;
    --card-white: #ffffff;
    --backdrop: #e9ebee;
    --card-w: 540px;
    --card-h: 309px;
  }
  * { box-sizing: border-box; margin: 0; padding: 0; }
  html, body { width: 1200px; height: 800px; overflow: hidden; }
  body {
    background: var(--backdrop);
    font-family: "Exo 2", Arial, sans-serif;
    display: flex;
    align-items: center;
    justify-content: center;
    gap: 40px;
  }
  .card {
    position: relative;
    width: var(--card-w);
    height: var(--card-h);
    background: var(--card-white);
    box-shadow: 0 6px 18px rgba(0,0,0,0.15);
    overflow: hidden;
  }

  /* Front */
  .card-front {
    display: flex;
    align-items: center;
    justify-content: center;
  }
  .wordmark {
    color: var(--brand-blue);
    font-weight: 700;
    font-size: 66px;
    letter-spacing: 3px;
    line-height: 1;
  }

  /* Back */
  .wave { position: absolute; inset: 0; width: 100%; height: 100%; }
  .wordmark-small {
    position: absolute;
    left: 30px; top: 32px;
    font-size: 40px;
    letter-spacing: 2px;
  }
  .contact-list {
    position: absolute;
    left: 34px; top: 128px;
    list-style: none;
  }
  .contact-item {
    display: flex;
    align-items: center;
    gap: 10px;
    color: var(--card-white);
    font-size: 15px;
    font-weight: 600;
    margin-bottom: 12px;
  }
  .icon-badge {
    width: 24px; height: 24px;
    border-radius: 50%;
    background: var(--brand-blue);
    display: flex; align-items: center; justify-content: center;
    flex: none;
  }
  .person {
    position: absolute;
    right: 40px; top: 130px;
    color: var(--brand-blue);
    font-weight: 600;
    font-size: 20px;
    line-height: 1.2;
  }
  .website {
    position: absolute;
    right: 34px; bottom: 30px;
    display: flex; align-items: center; gap: 10px;
    color: var(--card-white);
    font-weight: 600;
    font-size: 16px;
  }
</style>
</head>
<body>

  <section class="card card-front">
    <span class="wordmark">CORVALIN</span>
  </section>

  <section class="card card-back">
    <svg class="wave" viewBox="0 0 540 309" preserveAspectRatio="none">
      <path d="M0,92 C120,84 200,135 270,195 S420,268 540,262 L540,309 L0,309 Z" fill="#0a7bd0"/>
      <path d="M0,104 C115,100 190,150 258,208 S420,282 540,276 L540,309 L0,309 Z" fill="#8fd04a"/>
    </svg>

    <span class="wordmark wordmark-small">CORVALIN</span>

    <ul class="contact-list">
      <li class="contact-item">
        <span class="icon-badge">
          <svg width="13" height="13" viewBox="0 0 24 24"><path d="M6.6 10.8a15 15 0 0 0 6.6 6.6l2.2-2.2a1 1 0 0 1 1-.25 11.4 11.4 0 0 0 3.6.57 1 1 0 0 1 1 1V20a1 1 0 0 1-1 1A17 17 0 0 1 3 4a1 1 0 0 1 1-1h3.5a1 1 0 0 1 1 1c0 1.25.2 2.45.57 3.6a1 1 0 0 1-.25 1z" fill="#fff"/></svg>
        </span>PHONE
      </li>
      <li class="contact-item">
        <span class="icon-badge">
          <svg width="13" height="13" viewBox="0 0 24 24"><rect x="2" y="5" width="20" height="14" fill="#fff"/><path d="M2 5l10 8 10-8" fill="none" stroke="#0a7bd0" stroke-width="2"/></svg>
        </span>EMAIL
      </li>
    </ul>

    <div class="person">
      <div class="person-name">NAME</div>
      <div class="person-title">TITLE</div>
    </div>

    <div class="website">
      <span class="icon-badge">
        <svg width="14" height="14" viewBox="0 0 24 24" fill="none" stroke="#fff" stroke-width="2"><circle cx="12" cy="12" r="9"/><path d="M3 12h18M12 3c3 3 3 15 0 18M12 3c-3 3-3 15 0 18"/></svg>
      </span>www.corvalinbio.com
    </div>
  </section>

</body>
</html>
```